Rack Card for IV Infusion Vitamin Supplement bar

We need a very eye catching rack card so that customers would instantly know it is for IV vitamin infusions. We have our previous rack card (pdf) as an example that did not bring in any clients as an example as well as another one that we did not like too much. The bar is for people to feel better with hydration and vitamins.

Target Market(s)

Anyone

Industry/Entity Type

Healthcare

Requirements
Must have
• Logo on rack card
Should not have
• Not pink other than the logo

```html
<!DOCTYPE html>
<html lang="en">
<head>
<meta charset="utf-8">
<title>Orvia Health &amp; Wellness – Rack Card</title>
<link rel="stylesheet" href="https://fonts.googleapis.com/css2?family=Catamaran:wght@400;600;700;800&family=Philosopher:wght@700&family=Marcellus&display=swap">
<style>
  :root{
    --stage:#272727;
    --paper:#efede8;
    --white:#fbfbfa;
    --green:#0f5848;
    --blue:#2a9ad8;
    --ink:#1d1d1d;
    --pink:#d8408f;
    --orange:#f5a623;
  }
  *{box-sizing:border-box;margin:0;padding:0}
  html,body{width:751px;height:1200px;overflow:hidden;background:var(--stage)}
  body{font-family:"Catamaran",sans-serif;position:relative}
  .card{position:absolute;top:217px;width:340px;height:765px;background:var(--paper);overflow:hidden;box-shadow:0 10px 30px rgba(0,0,0,.45)}
  .card--front{left:25px}
  .card--back{left:386px}

  /* front */
  .front-shapes{position:absolute;inset:0}
  .hero-photo{position:absolute;left:0;top:120px;width:340px;height:340px;
    background:linear-gradient(135deg,#8a8580 0%,#c9c3bb 35%,#f4a21e 55%,#f7c04a 75%,#e48a10 100%)}
  .brand{position:absolute;top:52px;left:0;width:100%;display:flex;align-items:center;justify-content:center;gap:9px}
  .brand-dot{width:16px;height:16px;border-radius:50%;background:var(--pink)}
  .brand-name{font-family:"Marcellus",serif;font-size:23px;color:var(--green);letter-spacing:1px}
  .headline{position:absolute;top:466px;left:0;width:100%;text-align:center;font-family:"Philosopher",sans-serif;font-weight:700;line-height:1.05;font-size:34px}
  .headline .blue{color:var(--blue)}
  .headline .green{color:var(--green)}
  .book-now{position:absolute;top:582px;left:70px;width:200px;height:92px}
  .front-contact{position:absolute;bottom:10px;left:0;width:100%;text-align:center;color:#fff;line-height:1.3}
  .front-contact .phone{font-size:15px;font-weight:700}
  .front-contact .line{font-size:11.5px}
  .icon{display:inline-block;vertical-align:-2px;margin-right:3px}

  /* back */
  .menu{position:absolute;top:18px;left:22px;right:18px}
  .menu h2{font-weight:800;font-size:19px;color:var(--green);letter-spacing:.2px;line-height:1.1;margin-bottom:4px}
  .menu h2.addons{margin-top:14px}
  .item{margin-bottom:6px}
  .item.tight{margin-bottom:1px}
  .item h3{font-size:13.5px;font-weight:700;color:var(--blue);line-height:1.2;display:flex;align-items:center;gap:4px}
  .item h3::before{content:"";width:5px;height:5px;border-top:2px solid var(--green);border-right:2px solid var(--green);transform:rotate(45deg);flex:none;margin-right:1px}
  .item p{font-size:9.6px;color:var(--ink);line-height:1.32;padding-left:10px;max-width:290px}
  .fruit{position:absolute;border-radius:40% 60% 50% 50%;background:radial-gradient(circle at 40% 40%,#ffd36a,#f39a1a 60%,#e07a0c)}
  .fruit--wedge1{left:232px;top:322px;width:94px;height:62px}
  .fruit--wedge2{left:250px;top:440px;width:90px;height:68px}
  .fruit--c{left:236px;top:550px;width:92px;height:118px;border-radius:50%}
  .back-footer{position:absolute;bottom:0;left:0;width:100%;height:80px}
  .back-footer p{position:absolute;bottom:12px;width:100%;text-align:center;color:#fff;font-size:14.5px;font-weight:600;line-height:1.3}
</style>
</head>
<body>

<section class="card card--front" aria-label="Rack card front">
  <div class="hero-photo" role="img" aria-label="Photo of sliced oranges with a vitamin ampoule and syringe on marble"></div>
  <svg class="front-shapes" width="340" height="765" viewBox="0 0 340 765">
    <path d="M0 0H340V148Q165 218 0 152Z" fill="var(--white)"/>
    <path d="M0 154Q165 222 340 150" fill="none" stroke="var(--green)" stroke-width="2.5"/>
    <path d="M0 466Q160 392 340 446V765H0Z" fill="var(--paper)"/>
    <path d="M0 462Q160 388 340 442" fill="none" stroke="var(--green)" stroke-width="3"/>
    <path d="M0 704Q170 655 340 692V765H0Z" fill="var(--green)"/>
    <path d="M0 698Q170 648 340 686" fill="none" stroke="var(--blue)" stroke-width="3"/>
  </svg>
  <div class="brand"><span class="brand-dot"></span><span class="brand-name">Orvia Health &amp; Wellness</span></div>
  <h1 class="headline"><span class="blue">Vitamin</span><br><span class="green">Infusions And</span><br><span class="blue">Injections</span></h1>
  <svg class="book-now" viewBox="0 0 200 92" aria-label="Book now">
    <polygon points="30,2 198,2 178,50 2,50" fill="none" stroke="var(--blue)" stroke-width="3"/>
    <polygon points="36,6 192,6 172,46 14,46" fill="var(--green)"/>
    <polygon points="52,46 164,46 158,78 104,78 96,90 92,78 44,78" fill="var(--blue)"/>
    <text x="100" y="40" text-anchor="middle" font-family="Catamaran, sans-serif" font-weight="800" font-size="36" fill="#fff">BOOK</text>
    <text x="102" y="74" text-anchor="middle" font-family="Catamaran, sans-serif" font-weight="800" font-size="34" fill="#fff">NOW</text>
  </svg>
  <div class="front-contact">
    <div class="phone"><svg class="icon" width="12" height="12" viewBox="0 0 12 12"><circle cx="6" cy="6" r="5.3" fill="none" stroke="#fff" stroke-width="1.2"/><path d="M4 3.5l1 1.5-.6.7q.8 1.5 2 2l.7-.6 1.5 1-.6.9Q5 8.8 3.2 4.2Z" fill="#fff"/></svg>555-014-2298</div>
    <div class="line"><svg class="icon" width="11" height="11" viewBox="0 0 12 12"><circle cx="6" cy="6" r="5.3" fill="none" stroke="#fff" stroke-width="1.2"/><path d="M6 3a2 2 0 0 1 2 2c0 1.5-2 3.8-2 3.8S4 6.5 4 5a2 2 0 0 1 2-2Z" fill="#fff"/></svg>1420 W. Elm St Suite 2B Riverton, IN 46000</div>
    <div class="line"><svg class="icon" width="11" height="11" viewBox="0 0 12 12"><circle cx="6" cy="6" r="5.3" fill="none" stroke="#fff" stroke-width="1.2"/><path d="M1 6h10M6 1q-3 5 0 10M6 1q3 5 0 10" fill="none" stroke="#fff" stroke-width=".9"/></svg>www.orviatotalhealth.com</div>
  </div>
</section>

<section class="card card--back" aria-label="Rack card back">
  <div class="menu">
    <h2>PREMIUM INFUSIONS</h2>
    <div class="item"><h3>Orvia Cocktail</h3><p>Reduce stress, fatigue, and boost your energy. Orvia client favorite! (IV fluids, Vitamin C, B-complex, B12, &amp; electrolytes)</p></div>
    <div class="item"><h3>Immune Support</h3><p>Protect the immune system when risk of illness is high. Great for pre, post-travel (IV fluids, Vitamin C, B-complex, &amp; Zinc)</p></div>
    <div class="item"><h3>The Glow</h3><p>Give a glowing boost to skin and hair from inside out. (IV fluids, Glutathione, Vitamin B-complex, and Biotin)</p></div>
    <div class="item"><h3>Sports Recovery</h3><p>Recover fast from illness, exhaustion, and workouts. (IV fluids, B-complex, B12, and amino acids, and electrolytes)</p></div>
    <div class="item"><h3>Energized</h3><p>Boost metabolism, burn fat easier, and feel energized. (IV fluids, B-complex, and amino acid blend)</p></div>
    <div class="item"><h3>Brain Power</h3><p>Support overall brain function, increase memory recall and improve certain aspects of learning. (IV fluids, B6, alpha lipoic acid, and taurine)</p></div>
    <div class="item tight"><h3>The Jetlag Drip</h3></div>
    <div class="item tight"><h3>The Migraine / Pms Drip</h3></div>
    <div class="item tight"><h3>The Hangover Drip</h3></div>
    <div class="item"><h3>Nad+ 125g/ 250g/ 500g Drip</h3><p>Enhance your cognitive health and help reverse aging. Promotes cell regeneration. Can aid mental clarity, better sleep, and energy.</p></div>
    <div class="item"><h3>High Dose Vitamin C</h3><p>*Medical clearance required</p></div>
    <h2 class="addons">INFUSIONS ADD-ONS</h2>
    <div class="item"><h3>Glutathione</h3><p>*A powerful natural antioxidant to help Detox</p></div>
    <div class="item tight"><h3>Additional Vitamin C</h3></div>
    <div class="item tight"><h3>Additional Zinc</h3></div>
    <div class="item tight"><h3>Additional Magnesium</h3></div>
    <div class="item tight"><h3>Anti- Inflammation Medication</h3></div>
    <div class="item tight"><h3>Additional Zinc</h3></div>
    <div class="item tight"><h3>Additional Magnesium</h3></div>
    <div class="item tight"><h3>Anti- Inflammation Medication</h3></div>
  </div>
  <div class="fruit fruit--wedge1" role="img" aria-label="Orange wedge"></div>
  <div class="fruit fruit--wedge2" role="img" aria-label="Orange slice"></div>
  <div class="fruit fruit--c" role="img" aria-label="Orange slices arranged in the letter C"></div>
  <div class="back-footer">
    <svg width="340" height="80" viewBox="0 0 340 80" style="position:absolute;inset:0">
      <path d="M0 30Q170 -8 340 30V80H0Z" fill="var(--green)"/>
      <path d="M0 24Q170 -14 340 24" fill="none" stroke="var(--blue)" stroke-width="3"/>
    </svg>
    <p>By appointments only,<br>including weekends <svg class="icon" width="12" height="12" viewBox="0 0 12 12"><circle cx="6" cy="6" r="5.3" fill="none" stroke="#fff" stroke-width="1.2"/><path d="M4 3.5l1 1.5-.6.7q.8 1.5 2 2l.7-.6 1.5 1-.6.9Q5 8.8 3.2 4.2Z" fill="#fff"/></svg>555-014-2298</p>
  </div>
</section>

</body>
</html>
```